Harbor Rest Company Needs Business Card

Looking for a very nice looking business card. Creative but not extravagant. We sell beds and pillows across the U.S. and need something professional but catchy. I have attached the logo.

Name : Dale Morton
Title : President
Phone : (800) 417-2960
Email: rest@quiltano.com
Website: www.quiltano.com

Can be single-sided or double-sided
horizontal or vertical

Can use Blues/Greys

Target Market(s)

Mass Market

Industry/Entity Type

Retail

Contact Information for Business Card

Name : Dale Morton
Title : President
Phone : (800) 417-2960
Email: rest@quiltano.com
Website: www.quiltano.com

Requirements
Must have
• Clean, Modern, Smooth
• Can use Blues/Greys
• On the other side without the information - have something simple like www.quiltano.com or our logo
Nice to have
• Surprise me
Should not have
• Nothing crazy, nothing cluttered

```html
<!DOCTYPE html>
<html lang="en">
<head>
<meta charset="utf-8">
<title>Harbor Rest Company — Business Card</title>
<link href="https://fonts.googleapis.com/css2?family=Lato:wght@300;400;700&display=swap" rel="stylesheet">
<style>
  :root {
    --stage: #e9ecef;
    --card-blue: #3ba5d6;
    --ink: #3b4852;
    --paper: #ffffff;
    --rule: #4a5862;
  }
  * { box-sizing: border-box; margin: 0; padding: 0; }
  html, body {
    width: 1200px; height: 810px; overflow: hidden;
    background: var(--stage);
    font-family: "Lato", Arial, sans-serif;
  }
  .stage {
    width: 1200px; height: 810px;
    display: flex; align-items: center; justify-content: center; gap: 50px;
  }
  .card {
    position: relative;
    width: 540px; height: 310px;
    background: var(--card-blue);
    border-radius: 22px;
    box-shadow: 0 10px 28px rgba(30, 50, 70, 0.18);
  }
  .brand-name {
    position: absolute; left: 0; right: 0;
    text-align: center;
    color: var(--paper);
    font-weight: 300;
    letter-spacing: 1px;
    line-height: 1;
  }
  /* Front */
  .card-front .brand-name { top: 100px; font-size: 78px; }
  .front-web {
    position: absolute; left: 0; right: 0; bottom: 40px;
    display: flex; flex-direction: column; align-items: center; gap: 6px;
  }
  .front-web .swoosh { width: 230px; height: 6px; }
  .front-web .url { color: var(--ink); font-size: 13px; font-weight: 400; }
  .front-web .swoosh-low { width: 230px; height: 6px; }
  /* Back */
  .card-back .brand-name { top: 52px; font-size: 60px; }
  .person {
    position: absolute; left: 0; right: 0; top: 130px;
    text-align: center; line-height: 1.15;
  }
  .person-name { color: var(--ink); font-size: 21px; font-weight: 700; }
  .person-title { color: var(--paper); font-size: 13px; font-weight: 400; }
  .contact {
    position: absolute; left: 30px; right: 30px; top: 209px;
  }
  .contact::before {
    content: ""; position: absolute; left: 0; right: 0; top: 12px;
    height: 1px; background: var(--rule);
  }
  .contact-list {
    position: relative;
    display: flex; justify-content: center; align-items: flex-start; gap: 8px;
    list-style: none;
  }
  .contact-item {
    display: flex; flex-direction: column; align-items: center; gap: 10px;
    color: var(--ink); font-size: 16px; font-weight: 400; white-space: nowrap;
  }
  .contact-sep { color: var(--ink); font-size: 16px; padding-top: 35px; }
  .icon-dot {
    width: 25px; height: 25px; border-radius: 50%;
    background: var(--paper);
    display: flex; align-items: center; justify-content: center;
  }
  .icon-dot svg { width: 13px; height: 13px; fill: var(--rule); }
</style>
</head>
<body>
<main class="stage">
  <section class="card card-front" aria-label="Business card front">
    <div class="brand-name">quiltano</div>
    <div class="front-web">
      <svg class="swoosh" viewBox="0 0 230 6" aria-hidden="true"><path d="M0 3 Q115 1 230 3 Q115 4 0 3Z" fill="#ffffff"/></svg>
      <span class="url">www.quiltano.com</span>
      <svg class="swoosh-low" viewBox="0 0 230 6" aria-hidden="true"><path d="M0 3 Q115 2 230 3 Q115 5 0 3Z" fill="#ffffff"/></svg>
    </div>
  </section>

  <section class="card card-back" aria-label="Business card back">
    <div class="brand-name">quiltano</div>
    <div class="person">
      <div class="person-name">Dale Morton</div>
      <div class="person-title">President</div>
    </div>
    <div class="contact">
      <ul class="contact-list">
        <li class="contact-item">
          <span class="icon-dot"><svg viewBox="0 0 24 24" aria-hidden="true"><path d="M6.6 10.8a15.1 15.1 0 0 0 6.6 6.6l2.2-2.2c.3-.3.7-.4 1-.2 1.1.4 2.3.6 3.6.6.6 0 1 .4 1 1V20c0 .6-.4 1-1 1A17 17 0 0 1 3 4c0-.6.4-1 1-1h3.5c.6 0 1 .4 1 1 0 1.3.2 2.5.6 3.6.1.3 0 .7-.2 1z"/></svg></span>
          (800) 417-2960
        </li>
        <li class="contact-sep">|</li>
        <li class="contact-item">
          <span class="icon-dot"><svg viewBox="0 0 24 24" aria-hidden="true"><path d="M2 5h20v14H2z M3.5 6.5 12 13l8.5-6.5" fill="none" stroke="#4a5862" stroke-width="2"/></svg></span>
          rest@quiltano.com
        </li>
        <li class="contact-sep">|</li>
        <li class="contact-item">
          <span class="icon-dot"><svg viewBox="0 0 24 24" aria-hidden="true"><g fill="none" stroke="#4a5862" stroke-width="2"><circle cx="12" cy="12" r="9"/><ellipse cx="12" cy="12" rx="4" ry="9"/><path d="M3 12h18"/></g></svg></span>
          www.quiltano.com
        </li>
      </ul>
    </div>
  </section>
</main>
</body>
</html>
```